Fern Gully Cleaning Tablets needs 4 x labels

We're about to launch a very exciting cleaning product to market and need your help to brand the 4 x bottles. www.saltwren.com.au will change the way people buy and use household cleaning products whilst significantly reducing the impact on the earth.

The tablets are dropped into the long life recycled plastic bottle, you simply add water, wait for the tab to dissolve and begin cleaning.

Target Market(s)

Women aged between 30 - 65, care for the environment, want to use less plastic, are early adopters and like to try new things. Care about a clean home and using less chemicals. Want less packaging, less plastic, less carbon emissions.

Industry/Entity Type

House Cleaning

Font styles to use
Sans Serif

Requirements
Must have
• Each label must have an obvious colour differentiator and each label must be identical in it's dimensions and information. Should look uniform when all 4 bottles are aligned in the cupboard. Limited / no images apart from logo.
Nice to have
• Simple, clear, bold, striking. Limited / no pictures. Clean lines with lots of space.
Should not have
• Sparkvane Glass Label must have a strip of blue (hex BAE1FF).
Grease Ranger Kitchen Cleaner must have a strip of colour (FFD6F3)
The Fizzer Bathroom cleaner must have a colour strip hex # FFFFBA
The Allrounder Multip Purpose must have a strip of colour Hex #BAFFC9

```html
<!DOCTYPE html>
<html lang="en">
<head>
<meta charset="utf-8">
<title>Saltwren Cleaning Tablets – Bottle Labels</title>
<link rel="stylesheet" href="https://fonts.googleapis.com/css2?family=Source+Sans+3:wght@400;700&display=swap">
<style>
  :root {
    --ink: #005060;
    --page: #ffffff;
    --glass: #bae1ff;
    --kitchen: #ffd6f3;
    --bathroom: #ffffba;
    --multi: #baffc9;
  }
  * { margin: 0; padding: 0; box-sizing: border-box; }
  html, body {
    width: 1200px; height: 1000px; overflow: hidden;
    background: var(--page);
    font-family: "Source Sans 3", "Source Sans Pro", sans-serif;
    color: var(--ink);
  }
  .sheet { position: relative; width: 1200px; height: 1000px; }
  .label {
    position: absolute;
    width: 515px; height: 397px;
    border-radius: 10px;
    text-align: center;
  }
  .label--glass    { left: 60px;  top: 85px;  background: var(--glass); }
  .label--kitchen  { left: 627px; top: 85px;  background: var(--kitchen); }
  .label--bathroom { left: 57px;  top: 518px; background: var(--bathroom); }
  .label--multi    { left: 627px; top: 518px; background: var(--multi); }

  .label > * { position: absolute; left: 0; right: 0; }

  .brand {
    top: 40px;
    display: flex; align-items: center; justify-content: center; gap: 12px;
    font-size: 52px; font-weight: 700; line-height: 1;
  }
  .brand__dot {
    width: 22px; height: 22px; border-radius: 50%;
    background: var(--ink);
  }
  .divider {
    top: 138px; height: 5px;
    background: var(--ink);
  }
  .product-name {
    top: 162px;
    font-size: 44px; font-weight: 700; line-height: 1;
  }
  .product-type {
    top: 208px;
    font-size: 20px; font-weight: 700; line-height: 1;
  }
  .tagline {
    top: 256px;
    font-size: 12px; line-height: 15px;
  }
  .volume {
    top: 312px;
    font-size: 14px; line-height: 1;
  }
  .origin {
    top: 352px;
    font-size: 12px; line-height: 1;
  }
</style>
</head>
<body>
<main class="sheet">

  <section class="label label--glass">
    <div class="brand"><span>Saltwren</span><span class="brand__dot"></span></div>
    <div class="divider"></div>
    <h2 class="product-name">Sparkvane</h2>
    <p class="product-type">Window Cleaner</p>
    <p class="tagline">One Bottle - One Tab<br>Dissolve - Clean - Repeat</p>
    <p class="volume">500 ml</p>
    <p class="origin">Kestrel Heads.&nbsp; Australia</p>
  </section>

  <section class="label label--kitchen">
    <div class="brand"><span>Saltwren</span><span class="brand__dot"></span></div>
    <div class="divider"></div>
    <h2 class="product-name">Grease Ranger</h2>
    <p class="product-type">Kitchen Cleaner</p>
    <p class="tagline">One Bottle - One Tab<br>Dissolve - Clean - Repeat</p>
    <p class="volume">500 ml</p>
    <p class="origin">Kestrel Heads.&nbsp; Australia</p>
  </section>

  <section class="label label--bathroom">
    <div class="brand"><span>Saltwren</span><span class="brand__dot"></span></div>
    <div class="divider"></div>
    <h2 class="product-name">The Fizzer</h2>
    <p class="product-type">Bathroom Cleaner</p>
    <p class="tagline">One Bottle - One Tab<br>Dissolve - Clean - Repeat</p>
    <p class="volume">500 ml</p>
    <p class="origin">Kestrel Heads.&nbsp; Australia</p>
  </section>

  <section class="label label--multi">
    <div class="brand"><span>Saltwren</span><span class="brand__dot"></span></div>
    <div class="divider"></div>
    <h2 class="product-name">The Allrounder</h2>
    <p class="product-type">Multi Purpose Cleaner</p>
    <p class="tagline">One Bottle - One Tab<br>Dissolve - Clean - Repeat</p>
    <p class="volume">500 ml</p>
    <p class="origin">Kestrel Heads.&nbsp; Australia</p>
  </section>

</main>
</body>
</html>
```